High-end Oceanfront Real Estate Group Needs Clean, Modern Web Design

I’m looking for a clean, professional, modern and beautiful homepage web design for a Real Estate group in Southern California, USA.

The group/company is “Marlow on the Shore,” and they specialize in high end (i.e. expensive), oceanfront real estate in the Orange County area.

The look and feel of the page should accentuate the brand qualities: luxurious/expensive, professional, and beautiful (Orange County is one of the most beautiful areas in all the US and we would love the site to emphasize the beautiful beaches and scenery it has to offer).

Looks we like:
• www.brantleyhomesrealty.example
• www.keptbyfenwick.example -- I think the design is pretty out-dated in this site, but I like the organization/layout of the site

Header Tags (I don’t know if we can fit all of these, may need a side-menu, but I’d prefer header title only if possible):
• Welcome
• Featured Listings
• Previously Sold
• Sell
• Property Search
• Team
• Videos
• Blog
• Explore O.C.
• Contact

I have attached the beach and logo pics that we would like to use as the header, a few pictures of the team, and one sample home/view pic which can be used in any of the other sections (for pictures of the homes, just find expensive oceanfront houses and that will be fine).

I promise to provide feedback to each and every design submission. I appreciate the hard work that all of you are putting into your designs. There can be only one contest winner, but I hope to give all of you helpful feedback to submit the best designs possible!

Target Market(s)

Very wealthy home owners of oceanfront properties. These properties are worth several millions of dollars, and thus the site and brand needs to be targeted to very wealthy, successful individuals and families (both US and international buyers).

Industry/Entity Type

Real Estate

Number of Pages Required

2 page

Requirements
Must have
• I don’t want to give too many requirements, because I want to let you all be creative. However, here are the few Must Haves:
• Must submit 2 page designs (a home page and a sub page)
• Must use logo provided
• Focus is mostly on homes, but I would like to include some beach/ocean imagery as well
• The first “item” on the home page should be an accordion/slider which shows pictures of homes and with 1 line of text: “List with the Leader” and two link buttons: “Sell Your Home” and “Buy Your Home”
• Color palette needs to be mainly blues--to match ocean and sky blue
• Exported in all major formats (psd,ai,eps,png,jpeg,etc)
Nice to have
• We don’t necessarily need all of these, but would like to feature most:
• List of videos
• “Meet the Team”—brief team bios and pics
• Link(s) to Blog
• “List with the Leader” – section on why they should choose this firm
• Featured Listings
• Previously Sold

```html
<!DOCTYPE html>
<html lang="en">
<head>
<meta charset="utf-8">
<title>Marlow on the Shore — Oceanfront Real Estate</title>
<link href="https://fonts.googleapis.com/css2?family=Titillium+Web:wght@300;400;600;700&display=swap" rel="stylesheet">
<style>
  :root{
    --page:#eef2f6;
    --white:#ffffff;
    --brand:#3a84a8;
    --sky:#7fd0ef;
    --aqua:#44c9c6;
    --ink:#3b4650;
    --muted:#8a949c;
    --line:#d6dde3;
    --bar:#2b3a47;
    --field:#4b6379;
    --band:#2e6f92;
    --band-dark:#24536e;
    --foot:#dde2e7;
  }
  *{margin:0;padding:0;box-sizing:border-box}
  html,body{width:816px;height:1200px;overflow:hidden}
  body{background:var(--page);font-family:"Titillium Web",sans-serif;color:var(--ink);position:relative}

  /* header */
  .site-header{position:absolute;left:0;top:0;width:816px;height:66px;background:var(--page)}
  .brand{position:absolute;left:158px;top:8px;display:flex;align-items:flex-start;gap:5px}
  .brand-mark{width:12px;height:12px;background:var(--brand);margin-top:2px}
  .brand-name{color:var(--brand);font-weight:300;font-size:15px;line-height:15px;letter-spacing:.5px;text-transform:uppercase}
  .tagline{position:absolute;left:158px;top:53px;font-size:6px;color:var(--ink);letter-spacing:.3px}
  .contact{position:absolute;left:462px;top:21px}
  .contact .phone{font-size:13px;color:#555;display:flex;align-items:center;gap:4px;line-height:14px}
  .contact .phone svg{display:block;flex:none}
  .contact .email{font-size:5px;color:var(--muted);margin-left:9px}
  .list-btn{position:absolute;left:563px;top:20px;width:96px;height:24px;background:var(--sky);border-radius:2px;font-size:7px;color:#2a4a5c;display:flex;align-items:center;justify-content:center;gap:3px}

  /* nav */
  .main-nav{position:absolute;left:0;top:66px;width:816px;height:32px;border-top:1px solid var(--line)}
  .main-nav ul{list-style:none;position:absolute;left:158px;top:0;height:32px;display:flex}
  .main-nav li{font-size:6px;text-transform:uppercase;color:var(--ink);height:32px;display:flex;align-items:center;padding:0 8.4px}
  .main-nav li.active{background:var(--white);color:var(--brand);padding:0 11px}

  /* hero */
  .hero{position:absolute;left:0;top:98px;width:816px;height:247px;background:linear-gradient(180deg,#1d3a7e 0%,#2f5ea8 28%,#6d8fb4 46%,#9b8b6e 62%,#6f5a40 78%,#2f3d49 100%)}
  .hero-title{position:absolute;left:0;width:816px;top:176px;text-align:center;color:var(--white);font-weight:300;font-size:28.5px;letter-spacing:1px;line-height:40px}
  .hero-btn{position:absolute;top:232px;height:26px;border-radius:3px;color:#1d3d4c;font-size:9px;display:flex;align-items:center;justify-content:center}
  .hero-btn b{font-weight:700}
  .hero-btn.sell{left:303px;width:99px;background:#6ccbd8}
  .hero-btn.buy{left:416px;width:98px;background:var(--aqua)}
  .hero-arrow{position:absolute;top:205px}

  /* search */
  .search-bar{position:absolute;left:0;top:345px;width:816px;height:39px;background:var(--bar)}
  .select{position:absolute;top:10px;width:95px;height:18px;background:var(--field);color:#a9b8c5;font-size:5.5px;padding-left:5px;display:flex;align-items:center}
  .select::after{content:"";position:absolute;right:0;top:0;width:8px;height:18px;background:#5c7489}
  .range-label{position:absolute;left:475px;top:6px;width:100px;font-size:5px;color:#c6d2dc;display:flex;justify-content:space-between}
  .range-track{position:absolute;left:475px;top:18px;width:100px;height:3px;background:#c9d3db;border-radius:2px}
  .range-fill{position:absolute;left:0;top:0;width:77px;height:3px;background:var(--sky);border-radius:2px}
  .range-knob{position:absolute;top:-2px;width:6px;height:7px;background:var(--white);border-radius:1px}
  .search-btn{position:absolute;left:587px;top:10px;width:72px;height:18px;background:var(--sky);color:#1f3d4d;font-size:6px;font-weight:700;display:flex;align-items:center;justify-content:center}

  /* section headings */
  .section-title{position:absolute;left:158px;width:501px;display:flex;align-items:center;gap:8px;font-size:15px;font-weight:300;color:var(--ink);text-transform:uppercase;line-height:20px}
  .section-title::before,.section-title::after{content:"";flex:1;height:1px;background:var(--line)}
  .circle-arrow{width:9px;height:9px;border-radius:50%;background:#6cc1dd;display:flex;align-items:center;justify-content:center}

  /* properties */
  .property-grid{position:absolute;left:158px;top:426px;width:501px;height:338px;display:grid;grid-template-columns:repeat(4,1fr);grid-template-rows:repeat(3,1fr)}
  .photo{width:100%;height:100%}
  .featured{grid-column:1/3;grid-row:1/3;position:relative;background:linear-gradient(180deg,#8cc4e6 0%,#4fb8d6 30%,#2fb0b8 45%,#6a4a2e 62%,#3e2a1c 100%)}
  .featured .caption{position:absolute;left:9px;bottom:10px;right:9px;color:var(--white)}
  .featured h3{font-weight:400;font-size:12px;line-height:13px;width:120px}
  .featured p{font-size:5.5px;line-height:7px;width:140px;margin-top:3px}
  .featured .rating{font-size:5.5px;margin-top:6px;display:flex;align-items:center;gap:4px}
  .featured .price{position:absolute;right:0;bottom:0;font-size:14px;font-weight:300}
  .card{background:var(--white);padding:14px 10px 0 10px}
  .card h4{font-size:8px;font-weight:400;line-height:10px;color:var(--ink)}
  .card p{font-size:5px;line-height:6.5px;color:var(--muted);margin-top:6px}
  .card .price{font-size:14px;font-weight:300;color:var(--ink);margin-top:13px}
  .stars{color:var(--white);letter-spacing:.5px;font-size:6px}

  /* team */
  .team{position:absolute;left:158px;top:803px;width:501px;height:44px;display:flex;gap:8px}
  .member{flex:1;background:var(--white);display:flex;align-items:center;gap:5px}
  .member .portrait{width:46px;height:44px;flex:none;background:linear-gradient(180deg,#dfe3e6,#b9c1c7)}
  .member h5{font-size:6px;font-weight:700;color:var(--brand);text-transform:uppercase;line-height:8px}
  .member span{font-size:6px;color:var(--muted);line-height:8px;display:block}

  /* previously sold */
  .sold{position:absolute;left:0;top:863px;width:816px;height:197px;background:var(--band)}
  .sold-map{position:absolute;left:60px;top:0;width:220px;height:197px;background:radial-gradient(ellipse at 40% 45%,rgba(255,255,255,.08),rgba(255,255,255,0) 70%)}
  .sold h2{position:absolute;left:158px;top:18px;font-weight:300;font-size:19px;line-height:20px;color:var(--white)}
  .sold-list{list-style:none;position:absolute;left:159px;top:67px}
  .sold-list li{font-size:7px;color:#e3eef4;height:21px;line-height:13px;padding-left:10px}
  .sold-list li.current{border-left:2px solid var(--sky);padding-left:8px}
  .slide{position:absolute;top:41px;width:195px;height:143px}
  .slide .photo{height:113px}
  .slide .meta{height:30px;background:var(--band-dark);padding:4px 6px;color:var(--sky)}
  .slide .meta h6{font-size:6.5px;font-weight:400;text-transform:uppercase;line-height:9px}
  .slide .meta .row{display:flex;justify-content:space-between;align-items:center;margin-top:3px}
  .slide .meta .price{color:var(--white);font-size:6.5px}
  .slide-arrow{position:absolute;top:92px;width:17px;height:17px;background:#7cc6e6;display:flex;align-items:center;justify-content:center}

  /* partners */
  .partners{position:absolute;left:158px;top:1104px;width:501px;height:52px;background:var(--white);display:flex;align-items:center;justify-content:space-around}
  .partner{display:flex;align-items:center;gap:4px;font-size:9px;font-weight:600;color:var(--brand)}
  .partner i{display:block;width:9px;height:9px;background:var(--brand)}

  .site-footer{position:absolute;left:0;top:1178px;width:816px;height:22px;background:var(--foot);font-size:6px;color:var(--ink);display:flex;align-items:center;justify-content:center;text-transform:uppercase}
</style>
</head>
<body>

<header class="site-header">
  <div class="brand">
    <span class="brand-mark"></span>
    <span class="brand-name">Marlow<br>on the Shore</span>
  </div>
  <div class="tagline">LIVE.....WALK.....DREAM...</div>
  <div class="contact">
    <div class="phone">
      <svg width="6" height="10" viewBox="0 0 6 10" aria-hidden="true"><rect x="0" y="0" width="6" height="10" rx="1" fill="#666"/><rect x="1" y="1.3" width="4" height="6.2" fill="#eef2f6"/><rect x="2.3" y="8.2" width="1.4" height="1" fill="#eef2f6"/></svg>
      <span>949.555.0142</span>
    </div>
    <div class="email">hello@marlowontheshore.example</div>
  </div>
  <a class="list-btn">LIST YOUR PROPERTY
    <svg width="8" height="7" viewBox="0 0 8 7"><path d="M1 3.5 3 5.5 7 1" fill="none" stroke="#2a4a5c" stroke-width="1.5"/></svg>
  </a>
</header>

<nav class="main-nav">
  <ul>
    <li class="active">Home</li>
    <li>Featured Listings</li>
    <li>Previously Sold</li>
    <li>Sell</li>
    <li>Property Search</li>
    <li>Team</li>
    <li>Videos</li>
    <li>Blog</li>
    <li>Explore O.C.</li>
    <li>Contact</li>
  </ul>
</nav>

<section class="hero" role="img" aria-label="Oceanfront Mediterranean villa with a pool terrace and lounge chairs overlooking the coast under a blue sky"></section>
<svg class="hero-arrow" style="left:138px" width="22" height="42" viewBox="0 0 22 42"><path d="M20 1 2 21 20 41" fill="none" stroke="#fff" stroke-width="1.2"/></svg>
<svg class="hero-arrow" style="left:658px" width="22" height="42" viewBox="0 0 22 42"><path d="M2 1 20 21 2 41" fill="none" stroke="#fff" stroke-width="1.2"/></svg>
<h1 class="hero-title">LIST WITH THE LEADER</h1>
<a class="hero-btn sell">SELL YOUR&nbsp;<b>HOME</b></a>
<a class="hero-btn buy">BUY YOUR&nbsp;<b>HOME</b></a>

<form class="search-bar">
  <div class="select" style="left:158px">Property Status</div>
  <div class="select" style="left:262px">Location</div>
  <div class="select" style="left:365px">Property Type</div>
  <div class="range-label"><span>Price Range</span><span>0 - $450000</span></div>
  <div class="range-track">
    <div class="range-fill"></div>
    <span class="range-knob" style="left:0"></span>
    <span class="range-knob" style="left:74px"></span>
  </div>
  <div class="search-btn">SEARCH HERE</div>
</form>

<h2 class="section-title" style="top:399px">Recent Properties</h2>

<section class="property-grid">
  <article class="featured" role="img" aria-label="Wooden beach deck with a lounge chair and palms facing a turquoise sea">
    <div class="caption">
      <h3>Contrairement à une opinion répandue</h3>
      <p>Plusieurs variations de Lorem Ipsum peuvent être trouvées ici ou là, mais la majeure</p>
      <div class="rating">Rating: <span class="stars">★★★★☆</span></div>
      <div class="price">$ 420000</div>
    </div>
  </article>
  <div class="photo" role="img" aria-label="Modern curved beach house with an infinity pool at dusk" style="background:linear-gradient(180deg,#4aa0dc 0%,#2a74b8 45%,#1f5f96 70%,#3e8fb8 100%)"></div>
  <div class="card"><h4>Si vous voulez utiliser un passage du.</h4><p>Plusieurs variations de Lorem Ipsum peuvent être trouvées ici ou là, mais la majeure.</p><div class="price">$ 420000</div></div>
  <div class="card"><h4>Si vous voulez utiliser un passage du.</h4><p>Plusieurs variations de Lorem Ipsum peuvent être trouvées ici ou là, mais la majeure.</p><div class="price">$ 420000</div></div>
  <div class="photo" role="img" aria-label="White colonial house with a veranda beside a blue pool" style="background:linear-gradient(180deg,#2c5f8c 0%,#b9c6cc 45%,#6f9a8a 70%,#1fa4b6 100%)"></div>
  <div class="photo" role="img" aria-label="Villa terrace with an illuminated pool at sunset" style="background:linear-gradient(180deg,#e39a40 0%,#8c5a30 45%,#4a3a30 70%,#2a9bb8 100%)"></div>
  <div class="card"><h4>Si vous voulez utiliser un passage du.</h4><p>Plusieurs variations de Lorem Ipsum peuvent être trouvées ici ou là, mais la majeure.</p><div class="price">$ 420000</div></div>
  <div class="photo" role="img" aria-label="Aerial view of a red-roofed estate surrounded by palms near the beach" style="background:linear-gradient(180deg,#9ccbe0 0%,#4f8a4a 30%,#b4663e 55%,#3f7a3c 100%)"></div>
  <div class="card"><h4>Si vous voulez utiliser un passage du.</h4><p>Plusieurs variations de Lorem Ipsum peuvent être trouvées ici ou là, mais la majeure.</p><div class="price">$ 420000</div></div>
</section>

<h2 class="section-title" style="top:780px">
  <span class="circle-arrow"><svg width="4" height="5" viewBox="0 0 4 5"><path d="M4 0v5L0 2.5z" fill="#fff"/></svg></span>Meet the Team<span class="circle-arrow"><svg width="4" height="5" viewBox="0 0 4 5"><path d="M0 0v5l4-2.5z" fill="#fff"/></svg></span>
</h2>

<section class="team">
  <div class="member"><div class="portrait" role="img" aria-label="Team member portrait"></div><div><h5>Racines dans</h5><span>0800 555 0199</span></div></div>
  <div class="member"><div class="portrait" role="img" aria-label="Team member portrait"></div><div><h5>Les premières</h5><span>0800 555 0199</span></div></div>
  <div class="member"><div class="portrait" role="img" aria-label="Team member portrait"></div><div><h5>Utilisé depuis</h5><span>0800 555 0199</span></div></div>
  <div class="member"><div class="portrait" role="img" aria-label="Team member portrait"></div><div><h5>Finibus bonorum</h5><span>0800 555 0199</span></div></div>
</section>

<section class="sold">
  <div class="sold-map" role="img" aria-label="Faint map of the California and Mexico coastline"></div>
  <h2>Previously<br>Sold</h2>
  <ul class="sold-list">
    <li class="current">Contrairement</li>
    <li>Aune opinion</li>
    <li>Répandue</li>
    <li>Le Lorem</li>
    <li>Ipsum n'est</li>
    <li>Pas simplement</li>
  </ul>
  <article class="slide" style="left:261px">
    <div class="photo" role="img" aria-label="Balcony lounge chairs looking out over the ocean" style="background:linear-gradient(180deg,#d4e0e8 0%,#7fa2bb 35%,#4f7c9c 50%,#7a6a58 75%,#5a4a3c 100%)"></div>
    <div class="meta"><h6>Plusieurs variations de Lorem Ipsum</h6><div class="row"><span class="stars">★★★☆</span><span class="price">$ 420000</span></div></div>
  </article>
  <article class="slide" style="left:457px">
    <div class="photo" role="img" aria-label="Cliffside beach homes above a sandy cove" style="background:linear-gradient(180deg,#b3cde2 0%,#3a78a6 30%,#6f98b0 50%,#cfc2a6 72%,#e8e4dc 100%)"></div>
    <div class="meta"><h6>Plusieurs variations de Lorem Ipsum</h6><div class="row"><span class="stars">★★★☆</span><span class="price">$ 420000</span></div></div>
  </article>
  <div class="slide-arrow" style="left:256px"><svg width="6" height="7" viewBox="0 0 6 7"><path d="M5 0v7L0 3.5z" fill="#fff"/></svg></div>
  <div class="slide-arrow" style="left:639px"><svg width="6" height="7" viewBox="0 0 6 7"><path d="M1 0v7l5-3.5z" fill="#fff"/></svg></div>
</section>

<h2 class="section-title" style="top:1076px">List with the Leader</h2>

<section class="partners">
  <div class="partner"><i></i>Harbor Tours</div>
  <div class="partner"><i></i>Corvel Group</div>
  <div class="partner"><i></i>Tidewell</div>
  <div class="partner"><i></i>Brisa</div>
  <div class="partner"><i></i>Homeport Care</div>
</section>

<footer class="site-footer">Copyright © 2015 MarlowOnTheShore. All rights reserved.</footer>

</body>
</html>
```